Cover and back of brochure

Our company sells all kind of filters. Now we are planning to create an image brochure for our company. This brochure should represent our high quality standard, our competence and the trust of the clients in our company.

In the attachment I added covers of other catalogs which we like. Furthermore I added nice pictures in the attachment which were downloaded from glimmerdock. In the first place we downloaded these pictures in a small size, so that several examples can be created. After we decide which picture looks best on the cover, we will buy it in a higher resolution.

More information you find in the added pdf document.

Industry/Entity Type

It Company

Colors

Designer to choose colors to be used in the design.

```html
<!DOCTYPE html>
<html lang="de">
<head>
<meta charset="utf-8">
<title>Filter Hausner – Broschüre Umschlag</title>
<link rel="stylesheet" href="https://fonts.googleapis.com/css2?family=Oswald:wght@600&family=Arimo:wght@400;700&display=swap">
<style>
  :root {
    --slate: #3e4955;
    --white: #ffffff;
    --brand-green: #1f8a3a;
    --leaf-light: #d8ef9a;
    --leaf-mid: #8cc43c;
    --leaf-deep: #3f7d1c;
  }
  * { margin: 0; padding: 0; box-sizing: border-box; }
  html, body { width: 1200px; height: 848px; overflow: hidden; background: var(--slate); }
  .spread { position: relative; width: 1200px; height: 848px; background: var(--slate); }

  .back-cover { position: absolute; left: 0; top: 0; width: 600px; height: 848px; }
  .tagline {
    position: absolute; left: 0; width: 600px; top: 420px;
    text-align: center; color: var(--white);
    font: 600 22px/1 "Oswald", sans-serif; letter-spacing: 0.2px;
  }
  .contact {
    position: absolute; left: 0; width: 600px; top: 484px;
    text-align: center; color: var(--white);
    font: 400 11px/13.4px "Arimo", sans-serif;
  }
  .contact .strong { font-weight: 700; }

  .front-cover { position: absolute; left: 600px; top: 0; width: 600px; height: 848px; }
  .cover-photo {
    position: absolute; left: 0; top: 0; width: 600px; height: 718px;
    background:
      radial-gradient(circle at 8% 10%, rgba(255,255,230,0.85) 0, rgba(230,245,170,0.5) 18%, transparent 42%),
      radial-gradient(circle at 70% 45%, var(--leaf-mid) 0, transparent 55%),
      linear-gradient(160deg, var(--leaf-light) 0%, var(--leaf-mid) 45%, var(--leaf-deep) 100%);
  }
  .headline {
    position: absolute; right: 68px; top: 34px;
    color: var(--white); font: 600 21px/1 "Oswald", sans-serif;
  }
  .headline-mark {
    position: absolute; right: 14px; top: 20px; width: 46px; height: 46px;
    background: var(--white);
  }

  .brand-name {
    position: absolute; top: 772px; width: 600px; text-align: center;
    color: var(--brand-green); font: 700 24px/1 "Arimo", sans-serif;
  }
</style>
</head>
<body>
<main class="spread">
  <section class="back-cover">
    <p class="tagline">KOMPETENT• HILFSBEREIT•FREUNDLICH.</p>
    <address class="contact">
      <span class="strong">FILTER - HAUSNER e.K.</span><br>
      Inhaber Jens Adler<br>
      Lindenweg 14<br>
      10115 Berlin<br>
      Tel: 030 / 555 0140<br>
      Fax: 030 / 555 0141<br>
      E-Mail: info@filter-hausner.de<br>
      <span class="strong">Web: www.filter-hausner.de</span>
    </address>
    <p class="brand-name">Filter Hausner</p>
  </section>

  <section class="front-cover">
    <div class="cover-photo" role="img" aria-label="Photograph of sunlit fresh green beech leaves on a branch against a soft green background"></div>
    <h1 class="headline">FILTERKOMPETENZ HAT EINEN NAMEN</h1>
    <div class="headline-mark"></div>
    <p class="brand-name">Filter Hausner</p>
  </section>
</main>
</body>
</html>
```